Personal Trainer Business Card Design and Logo

I am a Personal Trainer and passionate in helping obese kids loose weight, I would love a business card design for my business called TOLV Fitness.
TOLV Ftiness stands for Tall Oaks Lively Ventures, I would like the business card to be bright and appealing to the kids as well as the parents.
I would also love a logo designs witch is simple but affective.

Things I would like in the business card
- Kids playing and being happy (no cartoon characters)
- The card should be bright and colourful
- My name, Bartholomew Van Hoek Personal Trainer
- Contact number 0472615809
- Email address tolvfitness@wexmail.test

Things I would like in the logo
-colourful design which incorporate kids
- your creative logo

thanks for all your entries
kind regards Bart
Updates

loving all the designs, you are all so talented.

could you please read the updated brief

kind regards

Bart

Reason: Loving the designs, but needs more modification kind reagrds Bart

Target Market(s)

Kids and Parents

Industry/Entity Type

Business

Contact Information for Business Card

TOLV Fitness for kids

Tall Oaks Lively Ventures

Bart Van Hoek Personal Trainer
0472615809

Requirements
Must have
• Kids laughing and happy, tolv fitness logo, Bart Van Hoek Personal Trainer, 0472615809,tolvfitness@wexmail.test, colourful and bright.
Nice to have
• pulse council mark

```html
<!DOCTYPE html>
<html lang="en">
<head>
<meta charset="utf-8">
<title>TOLV Fitness – Business Card Proof</title>
<link rel="stylesheet" href="https://fonts.googleapis.com/css2?family=Quicksand:wght@500;700&display=swap">
<style>
  :root{
    --bg-light:#ffffff;
    --bg-edge:#d9d9d9;
    --card-dark:#231f20;
    --text-white:#ffffff;
    --accent-yellow:#e6e21a;
    --rule-olive:#a8a23a;
    --sky-top:#6fa0d2;
    --sky-mid:#8fb8de;
    --sand:#c9b79a;
    --badge-red:#e3262f;
    --mark-black:#111111;
    --c:#00aeef; --m:#ec008c; --y:#fff200; --cm:#2e3192;
    --my:#ed1c24; --cy:#00a651; --cmy:#333333; --k:#1a1a1a;
  }
  *{margin:0;padding:0;box-sizing:border-box}
  html,body{width:1200px;height:1000px;overflow:hidden}
  body{
    position:relative;
    background:radial-gradient(ellipse at center,var(--bg-light) 45%,var(--bg-edge) 100%);
    font-family:"Quicksand",sans-serif;
  }
  .print-marks{position:absolute;left:0;top:0}
  .card{position:absolute;top:206px;width:309px;height:531px;overflow:hidden}
  .card--front{left:196px;background:var(--card-dark);color:var(--text-white);text-align:center}
  .card--back{left:689px;color:var(--text-white)}
  .tagline{font-weight:500;font-size:18px;letter-spacing:1.5px;text-transform:uppercase;white-space:nowrap}
  .card--front .tagline--top{position:absolute;top:47px;left:0;right:0}
  .card--front .brand{position:absolute;top:62px;left:0;right:0;font-weight:700;font-size:64px;line-height:70px;letter-spacing:4px;color:var(--accent-yellow)}
  .card--front .tagline--bottom{position:absolute;top:127px;left:0;right:0;font-size:15px}
  .trainer-name{position:absolute;top:240px;left:0;right:0;font-weight:500;font-size:22px;letter-spacing:.5px}
  .trainer-role{position:absolute;top:267px;left:0;right:0;font-size:13px;color:var(--accent-yellow);letter-spacing:.5px}
  .contact{position:absolute;top:356px;left:0;right:0;font-size:17px;letter-spacing:1.5px;line-height:23px}
  .contact-rule{position:absolute;top:411px;left:36px;width:236px;height:1px;background:var(--rule-olive)}
  .approval-badge{position:absolute;width:60px;height:60px;border-radius:50%;background:var(--badge-red);border:6px solid var(--text-white);box-shadow:0 0 0 1px #999}
  .card--front .approval-badge{left:124px;top:424px}
  .scene-photo{position:absolute;inset:0;background:linear-gradient(160deg,var(--sky-top) 0%,var(--sky-mid) 55%,var(--sand) 85%,var(--sand) 100%)}
  .brand-block{position:absolute;left:20px;top:88px;width:300px;transform:rotate(31deg);transform-origin:center;text-align:center}
  .brand-block .tagline{font-size:19px}
  .brand-block .brand{font-weight:700;font-size:110px;line-height:104px;letter-spacing:4px;color:var(--text-white)}
  .card--back .approval-badge{left:44px;top:424px}
</style>
</head>
<body>

<svg class="print-marks" width="1200" height="1000" viewBox="0 0 1200 1000" aria-hidden="true">
  <defs>
    <g id="reg-target">
      <circle r="9" fill="none" stroke="var(--mark-black)" stroke-width="1.3"/>
      <circle r="4.5" fill="var(--mark-black)"/>
      <line x1="-14" y1="0" x2="14" y2="0" stroke="var(--mark-black)" stroke-width="1"/>
      <line x1="0" y1="-14" x2="0" y2="14" stroke="var(--mark-black)" stroke-width="1"/>
    </g>
    <g id="star-target">
      <circle r="18" fill="var(--mark-black)"/>
      <circle r="12" fill="none" stroke="#ffffff" stroke-width="1.5" stroke-dasharray="2 2"/>
      <circle r="2.5" fill="#ffffff"/>
    </g>
    <g id="colour-bar">
      <rect y="0" width="30" height="29" fill="var(--c)"/>
      <rect y="29" width="30" height="29" fill="var(--m)"/>
      <rect y="58" width="30" height="29" fill="var(--y)"/>
      <rect y="87" width="30" height="29" fill="var(--cm)"/>
      <rect y="116" width="30" height="29" fill="var(--my)"/>
      <rect y="145" width="30" height="29" fill="var(--cy)"/>
      <rect y="174" width="30" height="29" fill="var(--cmy)"/>
      <rect y="203" width="30" height="32" fill="var(--k)"/>
      <rect width="30" height="235" fill="none" stroke="var(--mark-black)" stroke-width="1"/>
    </g>
    <g id="colour-bar-labelled" font-family="Quicksand, sans-serif" font-size="6" fill="#333" text-anchor="middle">
      <use href="#colour-bar"/>
      <text x="15" y="17">C</text><text x="15" y="46">M</text><text x="15" y="75">Y</text>
      <text x="15" y="104">CM</text><text x="15" y="133">MY</text><text x="15" y="162">CY</text>
      <text x="15" y="191">CMY</text><text x="15" y="221" fill="#bbb">K</text>
    </g>
    <g id="grey-ramp">
      <rect x="0" width="29" height="29" fill="#000"/>
      <rect x="29" width="29" height="29" fill="#1c1c1c"/>
      <rect x="58" width="29" height="29" fill="#363636"/>
      <rect x="87" width="29" height="29" fill="#4d4d4d"/>
      <rect x="116" width="29" height="29" fill="#666"/>
      <rect x="145" width="29" height="29" fill="#808080"/>
      <rect x="174" width="29" height="29" fill="#999"/>
      <rect x="203" width="29" height="29" fill="#b3b3b3"/>
      <rect x="232" width="29" height="29" fill="#ccc"/>
      <rect x="261" width="31" height="29" fill="#e6e6e6"/>
    </g>
    <g id="crop-set" stroke="var(--mark-black)" stroke-width="0.8">
      <line x1="-48" y1="16" x2="0" y2="16"/><line x1="309" y1="16" x2="357" y2="16"/>
      <line x1="-48" y1="514" x2="0" y2="514"/><line x1="309" y1="514" x2="357" y2="514"/>
      <line x1="16" y1="-46" x2="16" y2="0"/><line x1="293" y1="-46" x2="293" y2="0"/>
      <line x1="16" y1="531" x2="16" y2="579"/><line x1="293" y1="531" x2="293" y2="579"/>
    </g>
  </defs>

  <!-- front proof -->
  <use href="#crop-set" x="196" y="206"/>
  <use href="#star-target" x="173" y="185"/>
  <use href="#star-target" x="525" y="757"/>
  <use href="#reg-target" x="247" y="185"/>
  <use href="#reg-target" x="453" y="185"/>
  <use href="#reg-target" x="173" y="258"/>
  <use href="#reg-target" x="525" y="258"/>
  <use href="#reg-target" x="173" y="685"/>
  <use href="#reg-target" x="525" y="685"/>
  <use href="#colour-bar-labelled" x="158" y="354"/>
  <use href="#colour-bar" x="511" y="354"/>
  <use href="#grey-ramp" x="204" y="744"/>

  <!-- back proof -->
  <use href="#crop-set" x="689" y="206"/>
  <use href="#star-target" x="667" y="185"/>
  <use href="#star-target" x="1020" y="757"/>
  <use href="#reg-target" x="741" y="185"/>
  <use href="#reg-target" x="946" y="185"/>
  <use href="#reg-target" x="667" y="258"/>
  <use href="#reg-target" x="1020" y="258"/>
  <use href="#reg-target" x="667" y="685"/>
  <use href="#reg-target" x="1020" y="685"/>
  <use href="#colour-bar-labelled" x="652" y="354"/>
  <use href="#colour-bar" x="1005" y="354"/>
  <use href="#grey-ramp" x="697" y="744"/>
</svg>

<section class="card card--front">
  <p class="tagline tagline--top">Fitness for Kids</p>
  <p class="brand">TOLV</p>
  <p class="tagline tagline--bottom">Tall Oaks Lively Ventures</p>
  <p class="trainer-name">Bartholomew Van Hoek</p>
  <p class="trainer-role">Personal Trainer</p>
  <p class="contact">+047 261 58 09<br>tolvfitness@wexmail.test</p>
  <div class="contact-rule"></div>
  <div class="approval-badge" role="img" aria-label="pulse council mark"></div>
</section>

<section class="card card--back">
  <div class="scene-photo" role="img" aria-label="Photo of four girls in orange outfits jumping joyfully on a sunny beach under a blue sky"></div>
  <div class="brand-block">
    <p class="tagline">Fitness for Kids</p>
    <p class="brand">TOLV</p>
    <p class="tagline">Tall Oaks Lively Ventures</p>
  </div>
  <div class="approval-badge" role="img" aria-label="pulse council mark"></div>
</section>

</body>
</html>
```